Quorvane - corporate Business Card

We need a good look and innovative business card for a new start up company based in Los Angeles called "Quorvane". We are in a payment business, including payment card, app, and ewallet. We are expert in online payment and Card not present (CNP) transaction.
We need an innovative, modern business card.

Our logo font is Aero Matics

Target Market(s)

Startup - Bank - Online Payment - Card Manufacturing

Industry/Entity Type

Startup

Contact Information for Business Card

phone: 424 555 0173 - Address: 4270 Marbrook blvd, Halden Park, CA 90417

Requirements
Must have
• Message: innovative, professional, expert, high tech, trust, online payment expert, security
Nice to have
• no comment
Should not have
• no Comment

```html
<!DOCTYPE html>
<html lang="en">
<head>
<meta charset="utf-8">
<title>Quorvane – Business Card</title>
<link rel="stylesheet" href="https://fonts.googleapis.com/css2?family=Arimo:wght@400;700&display=swap">
<style>
  :root {
    --backdrop: #2a2a2a;
    --card: #f4f4f4;
    --card-edge: #e2e2e2;
    --brand-red: #b51f2e;
    --ink: #1c1c1c;
  }
  * { box-sizing: border-box; margin: 0; padding: 0; }
  html, body {
    width: 1200px; height: 997px; overflow: hidden;
    background: var(--backdrop);
    font-family: "Arimo", Arial, sans-serif;
  }
  .canvas { position: relative; width: 1200px; height: 997px; }
  .card {
    position: absolute;
    width: 580px; height: 331px;
    left: 310px;
    background: linear-gradient(160deg, #ffffff 0%, var(--card) 60%, var(--card-edge) 100%);
    border-radius: 22px;
    overflow: hidden;
    box-shadow: 0 18px 40px rgba(0,0,0,.45);
  }
  .card--front { top: 130px; }
  .card--back { top: 530px; }

  .front-mark {
    position: absolute; left: 50%; top: 50%;
    transform: translate(-50%, -50%);
    display: flex; align-items: center; gap: 18px;
  }
  .mark-dot {
    width: 74px; height: 74px; border-radius: 50%;
    background: var(--brand-red);
  }
  .mark-name {
    font-weight: 700; font-size: 58px; letter-spacing: 1px;
    color: var(--brand-red); line-height: 1;
  }

  .edge-band { position: absolute; background: var(--brand-red); }
  .edge-band--left { left: 0; top: 24px; width: 14px; height: 283px; border-radius: 0 8px 8px 0; }
  .edge-band--right { right: 0; top: 24px; width: 14px; height: 150px; border-radius: 8px 0 0 8px; }

  .back-mark {
    position: absolute; left: 40px; top: 0; width: 250px; height: 100%;
    display: flex; flex-direction: column; align-items: center; justify-content: center; gap: 16px;
  }
  .back-mark .mark-dot { width: 100px; height: 100px; }
  .back-mark .mark-name { font-size: 46px; }

  .divider {
    position: absolute; left: 310px; top: 40px; width: 2px; height: 250px;
    background: linear-gradient(to bottom, rgba(181,31,46,0), var(--brand-red) 50%, rgba(181,31,46,0));
  }

  .contact { position: absolute; left: 334px; top: 58px; width: 230px; }
  .contact__name {
    font-weight: 700; font-size: 16px; color: var(--brand-red); letter-spacing: .5px;
  }
  .contact__role { font-size: 13px; color: var(--ink); margin-top: 2px; }
  .contact__office {
    font-size: 14px; color: var(--brand-red); margin-top: 18px; line-height: 1.3;
  }
  .contact__list { list-style: none; margin-top: 18px; }
  .contact__item {
    display: flex; align-items: flex-start; gap: 10px;
    font-size: 14px; color: var(--ink); line-height: 1.3; margin-bottom: 8px;
  }
  .contact__icon { flex: none; width: 20px; height: 20px; margin-top: -1px; }
</style>
</head>
<body>
<main class="canvas">

  <section class="card card--front" aria-label="Card front">
    <div class="front-mark">
      <span class="mark-dot"></span>
      <span class="mark-name">quorvane</span>
    </div>
  </section>

  <section class="card card--back" aria-label="Card back">
    <span class="edge-band edge-band--left"></span>
    <span class="edge-band edge-band--right"></span>

    <div class="back-mark">
      <span class="mark-dot"></span>
      <span class="mark-name">quorvane</span>
    </div>

    <span class="divider"></span>

    <div class="contact">
      <p class="contact__name">DELPHINE HARROW</p>
      <p class="contact__role">Attorney</p>
      <p class="contact__office">4270 Marbrook blvd, Halden Park,<br>CA 90417</p>
      <ul class="contact__list">
        <li class="contact__item">
          <svg class="contact__icon" viewBox="0 0 20 20" aria-hidden="true">
            <circle cx="10" cy="10" r="10" fill="#b51f2e"/>
            <path d="M5 8.5c0-1.4 2.2-2.5 5-2.5s5 1.1 5 2.5v1h-2.6V8.3H7.6v1.2H5z M6.5 10.5h7l1 3.5h-9z" fill="#fff"/>
          </svg>
          <span>424 555 0173</span>
        </li>
        <li class="contact__item">
          <svg class="contact__icon" viewBox="0 0 20 20" aria-hidden="true">
            <circle cx="10" cy="10" r="10" fill="#b51f2e"/>
            <rect x="5" y="6.5" width="10" height="7" fill="#fff"/>
            <path d="M5 6.5l5 4 5-4" fill="none" stroke="#b51f2e" stroke-width="1"/>
          </svg>
          <span>4270 Marbrook blvd,<br>Halden Park, CA 90417</span>
        </li>
      </ul>
    </div>
  </section>

</main>
</body>
</html>
```